Communications Contractor Business Card Design

I would like a new business card for a new Communications company in Australia. Subcontracting and specialising in cabling, data, phone, antennas, pay tv ,modems, audio visual fibre optics etc. I am open to colour and design concepts but would like a modern clean look that stands out.

Industry/Entity Type

Tv

Contact Information for Business Card

kestrel communications pty ltd, Doug Pemberton, PO BOX 657 Marlow Flats QLD 4873 kestrel4me@maildrop-example.com Australia. ph 0437196084. Director/Technician. services- Cabling,data,phone,antennas,audio visual,home theatre, fibre optics.

```html
<!DOCTYPE html>
<html lang="en">
<head>
<meta charset="utf-8">
<title>Kestrel Communications – Business Card</title>
<link rel="stylesheet" href="https://fonts.googleapis.com/css2?family=Questrial&display=swap">
<style>
  :root {
    --page: #e9e6e1;
    --card-white: #f7f7f7;
    --brand-blue: #26b3ea;
    --charcoal: #3d3c3e;
    --ink-grey: #4a4a4c;
    --accent-orange: #e2602b;
    --white: #ffffff;
  }
  * { box-sizing: border-box; margin: 0; padding: 0; }
  html, body { width: 1200px; height: 672px; overflow: hidden; }
  body {
    background: var(--page);
    font-family: "Questrial", "Century Gothic", sans-serif;
    position: relative;
  }
  .card {
    position: absolute;
    left: 415px; top: 36px;
    width: 370px; height: 600px;
    background: var(--card-white);
    box-shadow: 0 6px 18px rgba(0,0,0,.18);
    overflow: hidden;
  }
  .top-bar {
    position: absolute; left: 12px; right: 12px; top: 0;
    height: 20px; background: var(--brand-blue);
    border-radius: 0 0 10px 10px;
  }
  .brand {
    position: absolute; right: 26px; top: 52px; text-align: right;
    color: var(--ink-grey);
  }
  .brand-name { font-size: 84px; line-height: 1; letter-spacing: 1px; }
  .brand-sub { font-size: 25px; margin-top: 2px; }
  .name-band {
    position: absolute; left: 0; right: 0; top: 196px; height: 64px;
    background: var(--brand-blue); border-radius: 14px 14px 0 0;
    color: var(--white); text-align: right; padding: 12px 26px 0 0;
    text-transform: uppercase;
  }
  .person-name { font-size: 20px; letter-spacing: 1px; }
  .person-role { font-size: 14px; letter-spacing: 1px; margin-top: 2px; }
  .rule { position: absolute; left: 0; right: 0; top: 260px; height: 3px; background: var(--accent-orange); }
  .details {
    position: absolute; left: 0; right: 0; top: 263px; height: 210px;
    background: var(--charcoal); padding: 28px 0 0 44px; color: var(--white);
  }
  .contact-list { list-style: none; }
  .contact-item { display: flex; align-items: center; gap: 10px; height: 30px; font-size: 14.5px; letter-spacing: .5px; }
  .contact-item svg { width: 20px; height: 20px; flex: none; }
  .contact-item.web { padding-left: 30px; font-size: 12.5px; }
  .address-band {
    position: absolute; left: 0; right: 0; top: 460px; height: 104px;
    background: var(--brand-blue); border-radius: 14px 14px 0 0;
    color: var(--white); display: flex; align-items: flex-start; gap: 12px;
    padding: 22px 0 0 44px; font-size: 15px; line-height: 1.5;
  }
  .address-band svg { width: 22px; height: 22px; flex: none; margin-top: 2px; }
</style>
</head>
<body>
  <article class="card">
    <div class="top-bar"></div>

    <header class="brand">
      <div class="brand-name">kestrel</div>
      <div class="brand-sub">Communications Pty Ltd</div>
    </header>

    <section class="name-band">
      <div class="person-name">Doug Pemberton</div>
      <div class="person-role">General Manager</div>
    </section>
    <div class="rule"></div>

    <section class="details">
      <ul class="contact-list">
        <li class="contact-item">
          <svg viewBox="0 0 20 20"><circle cx="10" cy="10" r="9" fill="none" stroke="#fff" stroke-width="1.4"/><path d="M7 5.5l2 2-1 1.2c.6 1.4 1.6 2.4 3 3l1.2-1 2 2-1.3 1.6c-3.4-.4-6.6-3.6-7-7z" fill="#fff"/></svg>
          <span>0437 196 084</span>
        </li>
        <li class="contact-item">
          <svg viewBox="0 0 20 20"><circle cx="10" cy="10" r="9" fill="none" stroke="#fff" stroke-width="1.4"/><rect x="7" y="4.5" width="6" height="11" rx="1" fill="#fff"/><rect x="8" y="6" width="4" height="6.5" fill="#3d3c3e"/></svg>
          <span>07 4055 1183</span>
        </li>
        <li class="contact-item">
          <svg viewBox="0 0 20 20"><circle cx="10" cy="10" r="9" fill="none" stroke="#fff" stroke-width="1.4"/><rect x="5" y="8" width="10" height="6" rx="1" fill="#fff"/><rect x="7" y="5" width="6" height="3" fill="#fff"/></svg>
          <span>07 4055 1184</span>
        </li>
        <li class="contact-item">
          <svg viewBox="0 0 20 20"><circle cx="10" cy="10" r="9" fill="none" stroke="#fff" stroke-width="1.4"/><circle cx="10" cy="10" r="2.6" fill="none" stroke="#fff" stroke-width="1.4"/><path d="M12.6 8v3a1.6 1.6 0 0 0 3 0V10a5.6 5.6 0 1 0-2.2 4.4" fill="none" stroke="#fff" stroke-width="1.3"/></svg>
          <span>kestrel4me@maildrop-example.com</span>
        </li>
        <li class="contact-item web"><span>www.kestrelcomms-example.com</span></li>
      </ul>
    </section>

    <section class="address-band">
      <svg viewBox="0 0 22 22"><circle cx="11" cy="11" r="10" fill="none" stroke="#fff" stroke-width="1.4"/><path d="M11 5a3.6 3.6 0 0 1 3.6 3.6c0 2.6-3.6 7-3.6 7s-3.6-4.4-3.6-7A3.6 3.6 0 0 1 11 5z" fill="#fff"/><circle cx="11" cy="8.6" r="1.3" fill="#26b3ea"/></svg>
      <address style="font-style:normal">PO BOX 657<br>Marlow Flats QLD 4873</address>
    </section>
  </article>
</body>
</html>
```